#VESSA

#Vessa is the business name. I need a marketing brochure to show potential clients. The concept is providing the restaurant trade and function centres with volume wine in large wine casks and then on-sell by the glass or in varying carafe sizes. The advantages will be outlined in the file provided I want to introduce the concept and demonstrate the advantages visusally

Industry/Entity Type

Restaurant

```html
<!DOCTYPE html>
<html lang="en">
<head>
<meta charset="utf-8">
<title>#Vessa — Cask Wine for the Restaurant Trade</title>
<link rel="stylesheet" href="https://fonts.googleapis.com/css2?family=Cinzel:wght@400&display=swap">
<style>
  :root {
    --brown: #3b2115;
    --cream: #f3e9dc;
    --gold: #e2b468;
    --wine-dark: #2a0206;
    --wine-mid: #7a0a14;
    --wine-bright: #a8121f;
  }
  * { margin: 0; padding: 0; box-sizing: border-box; }
  html, body { width: 1200px; height: 848px; overflow: hidden; background: #1a0d08; }
  .brochure {
    position: relative;
    width: 1200px;
    height: 848px;
    overflow: hidden;
    font-family: "Cinzel", serif;
    font-weight: 400;
    color: var(--cream);
    text-transform: uppercase;
  }
  .hero-photo {
    position: absolute;
    inset: 0;
    background:
      radial-gradient(ellipse 260px 420px at 1075px 520px, #0e0204 0%, #0e0204 55%, transparent 75%),
      radial-gradient(circle at 960px 560px, #b3141f 0%, transparent 22%),
      radial-gradient(ellipse 520px 480px at 900px 360px, var(--wine-bright) 0%, var(--wine-mid) 45%, var(--wine-dark) 100%);
  }
  .panel-shape { position: absolute; inset: 0; }
  .content { position: absolute; left: 30px; top: 0; width: 660px; }
  .tagline {
    position: absolute; top: 38px; left: 0;
    font-size: 23px; line-height: 35px; letter-spacing: 0.6px; white-space: nowrap;
  }
  .divider { position: absolute; left: 0; width: 632px; height: 12px; }
  .divider-top { top: 154px; }
  .divider-bottom { top: 551px; }
  .intro {
    position: absolute; top: 180px; left: 0;
    font-weight: 400; font-size: 24px; line-height: 34px; letter-spacing: 0.8px;
  }
  .intro .concept { display: block; font-size: 32px; line-height: 40px; letter-spacing: 0.6px; }
  .advantages {
    position: absolute; top: 282px; left: 0; list-style: none;
    font-size: 18px; line-height: 28.7px; letter-spacing: 0.4px; white-space: nowrap;
  }
  .advantages li::before { content: "* "; }
  .details {
    position: absolute; top: 590px; left: 0;
    font-size: 18px; line-height: 28.8px; letter-spacing: 0.3px; white-space: nowrap;
  }
  .brand-name {
    position: absolute; left: 714px; top: 140px; width: 381px;
    text-align: center; font-size: 64px; font-weight: 400; line-height: 1;
    color: var(--cream);
    letter-spacing: 6px;
  }
</style>
</head>
<body>
<main class="brochure">
  <div class="hero-photo" role="img" aria-label="Photo of a red wine bottle and a filled wine glass against a deep red backdrop"></div>

  <svg class="panel-shape" width="1200" height="848" viewBox="0 0 1200 848" aria-hidden="true">
    <defs>
      <linearGradient id="edgeGold" x1="0" y1="0" x2="0" y2="1">
        <stop offset="0" stop-color="#c98a3f"/>
        <stop offset="0.35" stop-color="#f6dca0"/>
        <stop offset="0.7" stop-color="#d9a556"/>
        <stop offset="1" stop-color="#f0c981"/>
      </linearGradient>
    </defs>
    <path d="M0 0 H760 C700 90 672 190 684 300 C700 430 790 520 846 620 C880 690 900 770 912 848 H0 Z" fill="var(--brown)"/>
    <path d="M760 0 C700 90 672 190 684 300 C700 430 790 520 846 620 C880 690 900 770 912 848" fill="none" stroke="url(#edgeGold)" stroke-width="6"/>
  </svg>

  <section class="content">
    <p class="tagline">Providing the restaurant trade<br>with a more effective, economical<br>sustainable alternative to wine retail.</p>

    <svg class="divider divider-top" viewBox="0 0 632 12" aria-hidden="true">
      <line x1="0" y1="6" x2="276" y2="6" stroke="var(--cream)" stroke-width="2"/>
      <rect x="279" y="1" width="8" height="8" transform="rotate(45 283 5)" fill="var(--gold)"/>
      <line x1="294" y1="6" x2="632" y2="6" stroke="var(--cream)" stroke-width="2"/>
    </svg>

    <h2 class="intro">The advantages of using<span class="concept">#Vessa concept:</span></h2>

    <ul class="advantages">
      <li>The cask wine uses less storage space</li>
      <li>Eco friendly, no glass.</li>
      <li>Larger quantity better margins</li>
      <li>Longer shelf life</li>
      <li>No wastage</li>
      <li>More hygienic</li>
      <li>Wine sourced from reputable growers in<br>well-known regions of New Zealand, Barossa<br>Valley and Tasmania.</li>
    </ul>

    <svg class="divider divider-bottom" viewBox="0 0 632 12" aria-hidden="true">
      <line x1="0" y1="6" x2="276" y2="6" stroke="var(--cream)" stroke-width="2"/>
      <rect x="279" y="1" width="8" height="8" transform="rotate(45 283 5)" fill="var(--gold)"/>
      <line x1="294" y1="6" x2="632" y2="6" stroke="var(--cream)" stroke-width="2"/>
    </svg>

    <p class="details">Cask sizes will start from 10ltrs and up to 22ltrs<br>aesthetic urns or wine barrels to hide cask that will come<br>in either 15ltr, 25ltr and will fit all cask sizes.<br>Carafe glassware available too: in 250ml, 500ml and 1000ml<br>sizes.</p>
  </section>

  <h1 class="brand-name">#Vessa</h1>
</main>
</body>
</html>
```